Bluestone Advisory & Mgmt - Professional Business Cards

Hi!

I am a Real Estate Developer and Construction Consultant.

I have a lot of inspiration from previous designs and would be open to using the attached Designs as a starting point. I would like to see these styles incorporated into your designs.

I really need professional business card to go with it that includes my important info.

Look forward to seeing your designs!.

Target Market(s)

My Target market are building owners, lawyers, consultants.

Industry/Entity Type

Real Estate Development

Contact Information for Business Card

My Name: Daniel Korvash
My Title: Principle
Company Name: Bluestone Advisory & Mgmt, LLC
Address: 348 West 41st Street, 7th FL New York, NY 10036
Mobile: 917.608.3719
Website: bam-hqx.com

Font styles to use
Serif
Sans Serif

Colors

Designer to choose colors to be used in the design.

Requirements
Must have
• Must incorporate the logo attached or have new that looks similar.
• Must use professional font that will be seen and judged by wealthy land owners and developers.
• Must incorporate some of the color green.
Should not have
• Photo's or pictures of people or buildings of any kind.

```html
<!DOCTYPE html>
<html lang="en">
<head>
<meta charset="utf-8">
<title>Bluestone Advisory &amp; Mgmt – Business Cards</title>
<link rel="stylesheet" href="https://fonts.googleapis.com/css2?family=Arimo:wght@700&family=Raleway:wght@500&family=Source+Sans+3:wght@400&display=swap">
<style>
  :root {
    --green: #4db779;
    --grey: #9a9090;
    --text-grey: #8a8585;
    --paper: #ffffff;
    --backdrop: #dcdcdc;
  }
  * { box-sizing: border-box; margin: 0; padding: 0; }
  html, body {
    width: 1125px;
    height: 1200px;
    overflow: hidden;
    background: var(--backdrop);
  }
  .card {
    position: absolute;
    background: var(--paper);
    border-radius: 30px;
    overflow: hidden;
  }
  .card--front { left: 137px; top: 95px; width: 848px; height: 480px; }
  .card--back  { left: 145px; top: 624px; width: 838px; height: 496px; }

  .swoosh { position: absolute; inset: 0; width: 100%; height: 100%; }

  .holder {
    position: absolute;
    right: 50px;
    top: 26px;
    text-align: right;
    color: var(--paper);
    font-family: "Arimo", Arial, sans-serif;
    font-weight: 700;
  }
  .holder__name { font-size: 27px; letter-spacing: 0.5px; line-height: 1.2; }
  .holder__title { font-size: 24px; line-height: 1.3; }

  .brand {
    position: absolute;
    font-family: "Raleway", sans-serif;
    font-weight: 500;
    color: var(--green);
    line-height: 1.1;
  }
  .card--front .brand { left: 38px; top: 130px; font-size: 46px; }
  .card--back .brand { left: 0; right: 0; top: 150px; font-size: 62px; text-align: center; }

  .contact {
    position: absolute;
    left: 38px;
    top: 332px;
    font-family: "Source Sans 3", sans-serif;
    font-size: 20px;
    color: var(--text-grey);
    list-style: none;
  }
  .contact li { display: flex; align-items: center; height: 34px; letter-spacing: 0.4px; }
  .contact svg { width: 18px; height: 18px; margin-right: 12px; fill: none; stroke: var(--green); stroke-width: 1.8; }
  .contact .icon-fill { fill: var(--green); stroke: none; }

  .divider {
    position: absolute;
    left: 310px;
    top: 372px;
    width: 1px;
    height: 56px;
    background: var(--text-grey);
  }
  .address {
    position: absolute;
    left: 336px;
    top: 368px;
    font-family: "Source Sans 3", sans-serif;
    font-size: 20px;
    color: var(--text-grey);
    line-height: 33px;
    font-style: normal;
  }

  .website {
    position: absolute;
    left: 0; right: 0;
    top: 415px;
    text-align: center;
    font-family: "Source Sans 3", sans-serif;
    font-size: 26px;
    letter-spacing: 6px;
    color: var(--text-grey);
  }
</style>
</head>
<body>

<section class="card card--front">
  <svg class="swoosh" viewBox="0 0 848 480" aria-hidden="true">
    <path fill="var(--green)" d="M0,0 H848 V246 C620,118 300,40 0,70 Z"/>
    <path fill="var(--grey)" d="M0,80 C300,50 620,130 848,256 L848,278 C620,150 300,62 0,86 Z"/>
  </svg>

  <div class="holder">
    <p class="holder__name">DANIEL KORVASH</p>
    <p class="holder__title">Principle</p>
  </div>

  <p class="brand">Bluestone<br>Advisory &amp; Mgmt</p>

  <ul class="contact">
    <li>
      <svg viewBox="0 0 20 20"><circle cx="10" cy="10" r="8.5"/><path class="icon-fill" d="M7 5.5l2 2-1.2 1.3a7 7 0 0 0 3.4 3.4L12.5 11l2 2-1.6 1.6C9 14 6 11 5.4 7.1Z"/></svg>
      917.608.3719
    </li>
    <li>
      <svg viewBox="0 0 20 20"><rect x="2" y="5" width="16" height="11" rx="1"/><path d="M2 6l8 6 8-6"/></svg>
      office@bam-hqx.com
    </li>
    <li>
      <svg viewBox="0 0 20 20"><circle cx="10" cy="10" r="8"/><ellipse cx="10" cy="10" rx="3.5" ry="8"/><path d="M2 10h16M3.5 6h13M3.5 14h13"/></svg>
      www.bam-hqx.com
    </li>
  </ul>

  <span class="divider"></span>
  <address class="address">348 West 41st Street,<br>7th FL New York, NY 10036</address>
</section>

<section class="card card--back">
  <p class="brand">Bluestone<br>Advisory &amp; Mgmt</p>
  <p class="website">www.bam-hqx.com</p>
</section>

</body>
</html>
```